Is your Will up to date?

We need a flyer that invites people to ask themselves if their Will is up to date.
In addition it is a known fact that people do not adjust their Will as often as they should to reflect their current wishes and circumstances.
Also, a large number of people end up having their estate pay taxes
that could be avoided if correct planning is in place.
We are offering a free of charge service the carry out a check to make sure families have in place a Will that suits their needs and circumstances and that has taken into account the tax positions and impact fully with a view to having the estate as tax efficient as possible.
A Will service is also part of the family check up.

Below is the suggested text for the flyer

A Will is one of the most important documents that we should all have. Many people are aware that if they die without having made a Will, then intestate rules apply which means in simple terms, that family assets and cash could end up in the hands of the Treasury.

While many people have looked at and acted upon creating a Will, it is fair to say that for many, the terms and wishes of the Will are often outdated. It is easy to assume that amending a Will frequently is a complicated process which it need not be.

An individual or a family Will is most important in order to ensure that upon death, your estate is dealt with and distributed in accordance with your wishes. This is also to ensure that any family are looked after by those provisions. Not only may family changes and additions affect a family Will, but there are also life changing situations that can have an effect.

Additionally, consideration needs to be given regularly to the current tax position, with specific regard to Inheritance Tax and how estate values can be legitimately reduced resulting in less tax to pay.

At Thornbury & Company we have the advantage of our Chartered Accountancy practice background, as well as also being Independent Financial Advisers. We are therefore well placed to advise families on the creation or updating of their Will, and to give advice on how to minimise tax payments.

Even for individuals and families that have had no significant changes in circumstances for many years, very often the beneficiaries may need to be updated, and even the appointment of Executors and Trustees needs to be addressed because very often, these instructions are considerably out of date.

A Will and all of its complex implications should be reviewed every one or two years and it is an extremely simple process to do this with our assistance.

So far as minimising payments for tax there are a wide range of effective methods that help do this. As general examples, there can be gifts made to family or a partner, gifts to friends, charitable donations, the use of insurance products to help settle tax liability as well as looking at placing assets into Trust. We have a wealth of experience in setting up the different types of Trust that exist and can help you easily understand how they would work for you.

When looking at the preparation of a Will, there are hundreds of questions that could be considered appropriate. However, with our experience and knowledge, and bespoke software this process can be covered within an initial meeting of less than one hour. You will have the re-assurance of knowing that every aspect has been carefully considered in preparing a Will to your circumstances and wishes.

The initial meeting and any follow up meetings are completely free of all cost and charges, and can be held at either our offices, or at your home if preferred.

We can just as easily deal with the process over the telephone if more convenient. Thereafter, we will prepare a draft Will for you, and give you confirmation as to the charges. In most cases, an individual or family Will would not normally involve charges in excess of £100.

So far as mitigating possible Inheritance Tax liabilities on the estate, we also offer the benefit of an asset and investment review at no cost. The individual or family assets are carefully considered, along with your requirements of income and growth and any specific requests or wishes that you wish to build into any trust or other methods of your choosing.

At the initial meeting or conference call we discuss all of these implications and will prepare a report and recommendations for your consideration, again free of charge. If you decide to act upon any of the recommendations, then any fees can be discussed and agreed at that stage.

All in all, whether you require assistance in preparing or updating a Will, or receiving independent advice regarding your estate assets or investments, these functions are carried out by us at no initial costs or charges.

At every step of the way there are never hidden charges or fees that you will be asked to be paid. We have over 30 years of experience in these market places, and value the service we give our clients and the reputation we gain from it.

We consider the review of a Will should be carried out at a minimum of every two years and it is a very small financial budget to allow for, against having the satisfaction of knowing these important matters are reflecting your current views, circumstances and wishes.

The same can be said for any trust and investment matters and any estate advice given. We are extremely proud and confident of the service we provide, and if any of our clients decide they do not wish to act upon the advice given, then they at least have had the benefit of a thorough review together with a recommendation without obligations of any sort.

To discuss these matters further or to make arrangements for a meeting please call our offices or email to gareth@thornburyco-mail.co.uk
Updates

Content will be uploaded with next 24 hours

I am updating the brief with the wording.
It needs to be spread over the front and back of the flyer in an easy to read non boring design

Our firm logo will be updated shorty plus our Institute logo
Please make the flyer as catchy and interesting as possible.
Its a relatively boring topic for most people so it has to be eye catching rather than reading a page in a book

We will increase the budget if we are presented with a design we really like

Please note slightly amended text uploaded today

Target Market(s)

middle to upper class residents

Industry/Entity Type

Investment

Requirements
Must have
• Web address
Easy to read and understand
To look and feel catchy and not like reading a book
Some catchy graphics about tax, money, families etc

Fields where I can easily insert text and other details

```html
<!DOCTYPE html>
<html lang="en">
<head>
<meta charset="utf-8">
<title>Is your Will up to date? – Thornbury &amp; Company flyer</title>
<link rel="stylesheet" href="https://fonts.googleapis.com/css2?family=Alegreya+SC:wght@400;700&family=Crimson+Text:wght@400;600&display=swap">
<style>
  :root {
    --red: #d0111b;
    --ink: #2a2a2a;
    --paper: #ffffff;
    --backdrop: #d9d9d9;
    --steel-dark: #2b2b2b;
    --steel-mid: #6e6e6e;
    --photo-green: #7d9a4a;
    --photo-light: #c9d79a;
  }
  * { box-sizing: border-box; margin: 0; padding: 0; }
  html, body { width: 1200px; height: 790px; overflow: hidden; background: var(--backdrop); }
  body { font-family: "Crimson Text", Georgia, serif; color: var(--ink); }

  .spread {
    position: absolute; left: 20px; top: 20px; width: 1160px; height: 750px;
    background: var(--paper); box-shadow: 0 6px 18px rgba(0,0,0,.25); overflow: hidden;
  }
  .spine { position: absolute; left: 580px; top: 0; width: 1px; height: 100%; background: rgba(0,0,0,.08); z-index: 5; }

  .body-copy p { font-size: 9.4px; line-height: 1.26; text-align: justify; margin-bottom: 7px; }
  .section-heading {
    font-family: "Alegreya SC", Georgia, serif; color: var(--red);
    font-size: 12px; line-height: 1.2; margin: 0 0 8px;
  }

  /* left page */
  .left-copy { position: absolute; left: 30px; top: 36px; width: 392px; }
  .left-copy .section-heading { font-size: 13px; margin: 4px 0 9px; }
  .family-photo {
    position: absolute; left: 30px; top: 470px; width: 392px; height: 225px;
    background: linear-gradient(160deg, var(--photo-light), var(--photo-green) 70%, #56702f);
  }
  .left-band { position: absolute; left: 0; bottom: 0; width: 440px; height: 110px; }
  .call-line {
    position: absolute; left: 30px; bottom: 18px; display: flex; align-items: center; gap: 8px;
    font-family: "Alegreya SC", Georgia, serif; color: var(--paper); font-size: 15px; letter-spacing: .5px;
  }

  /* title column */
  .headline {
    position: absolute; left: 452px; top: 108px; width: 130px;
    font-family: "Alegreya SC", Georgia, serif; font-weight: 400; font-size: 33px; line-height: 1; color: var(--ink);
  }
  .headline .line { display: block; height: 35px; }
  .headline .highlight { display: inline-block; line-height: 1; background: var(--red); color: var(--paper); padding: 0 5px 2px; }

  /* centre photo */
  .pen-photo {
    position: absolute; left: 440px; top: 335px; width: 322px; height: 415px;
    background: radial-gradient(ellipse at 55% 40%, var(--steel-mid), var(--steel-dark) 75%);
  }

  /* right page */
  .right-top { position: absolute; left: 600px; top: 24px; width: 285px; }
  .right-lower { position: absolute; left: 780px; top: 345px; width: 345px; }
  .pull-quote {
    position: absolute; left: 900px; top: 34px; width: 235px;
    font-family: "Alegreya SC", Georgia, serif; font-size: 25px; line-height: 1.12; color: var(--ink);
  }
  .right-band { position: absolute; right: 0; bottom: 0; width: 398px; height: 190px; }
  .brand {
    position: absolute; right: 32px; bottom: 60px; width: 200px; padding: 7px 10px;
    background: var(--paper); display: flex; align-items: center; gap: 8px;
  }
  .brand-mark { width: 28px; height: 28px; background: var(--red); flex: none; }
  .brand-name { font-family: "Crimson Text", Georgia, serif; font-weight: 600; font-size: 16px; color: var(--ink); line-height: 1; }
  .brand-tagline { font-size: 8.5px; color: var(--ink); line-height: 1.2; margin-top: 2px; }
  .web-address {
    position: absolute; right: 32px; bottom: 26px;
    font-family: "Alegreya SC", Georgia, serif; color: var(--paper); font-size: 14px; letter-spacing: 1px;
  }
</style>
</head>
<body>
<main class="spread">
  <div class="spine"></div>

  <section class="left-copy body-copy">
    <p>A Will is one of the most important documents that we should all have. Many people are aware that if they die without having made a Will, then intestate rules apply which means in simple terms, that family assets and cash could end up in the hands of the Treasury.</p>
    <p>While many people have looked at and acted upon creating a Will, it is fair to say that for many, the terms and wishes of the Will are often outdated. It is easy to assume that amending a Will frequently is a complicated process which it need not be.</p>
    <p>An individual or a family Will is most important in order to ensure that upon death, your estate is dealt with and distributed in accordance with your wishes. This is also to ensure that any family are looked after by those provisions. Not only may family changes and additions affect a family Will, but there are also life changing situations that can have an effect.</p>
    <p>Additionally, consideration needs to be given regularly to the current tax position, with specific regard to Inheritance Tax and how estate values can be legitimately reduced resulting in less tax to pay.</p>
    <h2 class="section-heading">At Thornbury &amp; Company we have the advantage of our Chartered Accountancy practice background</h2>
    <p>At Thornbury &amp; Company we have the advantage of our Chartered Accountancy practice background, as well as also being Independent Financial Advisers. We are therefore well placed to advise families on the creation or updating of their Will, and to give advice on how to minimise tax payments.</p>
    <p>Even for individuals and families that have had no significant changes in circumstances for many years, very often the beneficiaries may need to be updated, and even the appointment of Executors and Trustees needs to be addressed because very often, these instructions are considerably out of date.</p>
  </section>

  <div class="family-photo" role="img" aria-label="Photo of three generations of a family sitting together outdoors in a sunny park"></div>

  <svg class="left-band" viewBox="0 0 440 110" preserveAspectRatio="none" aria-hidden="true">
    <path d="M0 40 Q220 70 440 20 L440 110 L0 110 Z" fill="var(--red)"/>
  </svg>
  <div class="call-line">
    <svg width="16" height="16" viewBox="0 0 24 24" aria-hidden="true">
      <path fill="#fff" d="M6.6 10.8a15.1 15.1 0 0 0 6.6 6.6l2.2-2.2a1 1 0 0 1 1-.25 11.4 11.4 0 0 0 3.6.57 1 1 0 0 1 1 1V20a1 1 0 0 1-1 1A17 17 0 0 1 3 4a1 1 0 0 1 1-1h3.5a1 1 0 0 1 1 1c0 1.25.2 2.45.57 3.6a1 1 0 0 1-.25 1Z"/>
    </svg>
    <span>Call us on 01632 960418</span>
  </div>

  <h1 class="headline">
    <span class="line">Is</span>
    <span class="line">your</span>
    <span class="line"><span class="highlight">Will</span></span>
    <span class="line">up</span>
    <span class="line">to</span>
    <span class="line">date?</span>
  </h1>

  <div class="pen-photo" role="img" aria-label="Close-up photo of a silver fountain pen nib resting on dark textured paper"></div>

  <section class="right-top body-copy">
    <h2 class="section-heading">A Will and all of its complex implications should be reviewed every one or two years and it is an extremely simple process to do this with our assistance.</h2>
    <p>A Will and all of its complex implications should be reviewed every one or two years and it is an extremely simple process to do this with our assistance.</p>
    <p>So far as minimising payments for tax there are a wide range of effective methods that help do this. As general examples, there can be gifts made to family or a partner, gifts to friends, charitable donations, the use of insurance products to help settle tax liability as well as looking at placing assets into Trust. We have a wealth of experience in setting up the different types of Trust that exist and can help you easily understand how they would work for you.</p>
    <p>When looking at the preparation of a Will, there are hundreds of questions that could be considered appropriate. However, with our experience and knowledge, and bespoke software this process can be covered within an initial meeting of less than one hour. You will have the re-assurance of knowing that every aspect has been carefully considered in preparing a Will to your circumstances and wishes.</p>
  </section>

  <blockquote class="pull-quote">In most cases, an individual or family Will would typically not involve charges in excess of £100.</blockquote>

  <section class="right-lower body-copy">
    <p>The initial meeting and any follow up meetings are completely free of all cost and charges, and can be held at either our offices, or at your home if preferred.</p>
    <p>We can just as easily deal with the process over the telephone if more convenient. Thereafter, we will prepare a draft Will for you, and give you confirmation as to the charges. In most cases, an individual or family Will would not normally involve charges in excess of £100.</p>
    <p>So far as mitigating possible Inheritance Tax liabilities on the estate, we also offer the benefit of an asset and investment review at no cost. The individual or family assets are carefully considered, along with your requirements of income and growth and any specific requests or wishes that you wish to build into any trust or other methods of your choosing.</p>
  </section>

  <svg class="right-band" viewBox="0 0 398 190" preserveAspectRatio="none" aria-hidden="true">
    <path d="M0 110 Q200 90 398 0 L398 190 L0 190 Z" fill="var(--red)"/>
  </svg>
  <div class="brand">
    <span class="brand-mark"></span>
    <div>
      <div class="brand-name">Thornbury &amp; Co.</div>
      <div class="brand-tagline">Chartered Accountants &amp; Independent Financial Advisers</div>
    </div>
  </div>
  <div class="web-address">www.thornburyco.co.uk</div>
</main>
</body>
</html>
```